agricultural technology company needs business cards*

design a business card that represents our business well. please see our website: vastrelbyfieldseal.com.au
professional, simple, clean lines, not complicated or floral.....

```html
<!DOCTYPE html>
<html lang="en">
<head>
<meta charset="utf-8">
<title>Vastrelby Fieldseal — Business Cards</title>
<link href="https://fonts.googleapis.com/css2?family=Montserrat:wght@400;500;700&display=swap" rel="stylesheet">
<style>
  :root {
    --bg: #1c1c1c;
    --navy: #1a2b5e;
    --navy-text: #1d2f66;
    --green: #26b04b;
    --lime: #9dcb3b;
    --white: #ffffff;
    --ink: #1d2f66;
  }
  * { margin: 0; padding: 0; box-sizing: border-box; }
  html, body { width: 1200px; height: 930px; overflow: hidden; }
  body {
    background: var(--bg);
    font-family: "Montserrat", Arial, sans-serif;
    position: relative;
  }
  .card {
    position: absolute;
    width: 560px;
    height: 320px;
    border-radius: 4px;
    overflow: hidden;
    box-shadow: 0 12px 30px rgba(0,0,0,0.55);
  }
  .card--front {
    left: 80px; top: 110px;
    background: var(--navy);
    display: flex; align-items: center; justify-content: center;
  }
  .card--back {
    left: 560px; top: 500px;
    background: var(--white);
  }
  .wordmark {
    display: flex; align-items: center; gap: 14px;
  }
  .wordmark__square {
    width: 34px; height: 34px; background: var(--green);
  }
  .wordmark__name {
    font-weight: 700;
    line-height: 1;
    letter-spacing: -0.5px;
  }
  .card--front .wordmark__name { color: var(--white); font-size: 40px; }
  .accent-band {
    position: absolute; top: 0; right: 0;
    width: 240px; height: 100%;
    background: var(--green);
  }
  .card--back .wordmark {
    position: absolute; left: 36px; top: 44px;
  }
  .card--back .wordmark__square { width: 22px; height: 22px; }
  .card--back .wordmark__name { color: var(--navy-text); font-size: 24px; }
  .contact {
    position: absolute; left: 40px; top: 130px;
  }
  .contact__marker {
    position: absolute; left: -40px; top: 2px;
    width: 14px; height: 40px; background: var(--green);
  }
  .contact__name {
    color: var(--lime);
    font-size: 22px; font-weight: 500;
    letter-spacing: 1.5px; text-transform: uppercase;
  }
  .contact__role {
    color: var(--ink); font-size: 12px; margin-top: 2px;
  }
  .contact__address {
    color: var(--ink); font-size: 12.5px; line-height: 1.45; margin-top: 14px;
  }
  .contact__lines { list-style: none; margin-top: 12px; }
  .contact__lines li {
    display: flex; align-items: center; gap: 8px;
    color: var(--ink); font-size: 12.5px; line-height: 1.55;
  }
  .contact__lines svg { width: 11px; height: 11px; flex: none; }
</style>
</head>
<body>

<section class="card card--front" aria-label="Card front">
  <div class="wordmark">
    <span class="wordmark__square"></span>
    <span class="wordmark__name">Vastrelby Fieldseal</span>
  </div>
</section>

<section class="card card--back" aria-label="Card back">
  <div class="accent-band"></div>
  <div class="wordmark">
    <span class="wordmark__square"></span>
    <span class="wordmark__name">Vastrelby Fieldseal</span>
  </div>
  <div class="contact">
    <span class="contact__marker"></span>
    <p class="contact__name">Darren Holloway</p>
    <p class="contact__role">Director</p>
    <p class="contact__address">52 Tamsin Road<br>Baldivis, WA 6171</p>
    <ul class="contact__lines">
      <li>
        <svg viewBox="0 0 12 12" aria-hidden="true"><path d="M3 1l2 2.5-1.2 1.2a7 7 0 0 0 3.5 3.5L8.5 7 11 9l-1.5 2C5 11 1 7 1 2.5z" fill="var(--green)"/></svg>
        1300 482 610
      </li>
      <li>
        <svg viewBox="0 0 12 12" aria-hidden="true"><rect x="1" y="2.5" width="10" height="7" fill="none" stroke="var(--green)" stroke-width="1.2"/><path d="M1 2.5l5 4 5-4" fill="none" stroke="var(--green)" stroke-width="1.2"/></svg>
        info@vastrelbyfieldseal.com.au
      </li>
      <li>
        <svg viewBox="0 0 12 12" aria-hidden="true"><circle cx="6" cy="6" r="4.8" fill="none" stroke="var(--green)" stroke-width="1.1"/><ellipse cx="6" cy="6" rx="2" ry="4.8" fill="none" stroke="var(--green)" stroke-width="1"/><path d="M1.2 6h9.6" stroke="var(--green)" stroke-width="1"/></svg>
        www.vastrelbyfieldseal.com.au
      </li>
    </ul>
  </div>
</section>

</body>
</html>
```